Business Card Design Project- Removalist

I would like to surprise my husband to be with a different type of wedding present. His brother (who he owned a removalist business with) suddenly passed away from cancer recently and he has changed his business name to 'RTB' (which stands for Raising Tom Bright; but the full name doesn't need to be on the business card as it is more of a personal business name). To celebrate the new business I would like to get him some business cards made.
I would like the business name to be listed as 'RTB' and somewhere on the card I would like 'Sydney wide removals and relocation services'. I would like it to be obvious from the front of the card that it is a removalist business card. If a truck or some other feature that makes it look like a removalist business card could added it would be appreciated.
I don't mind what colours are used, but I would like the colour blue to feature somewhere in the design. It can be bright and fun, which is how Tom was.
I will also need the company's email address and phone number listed
The email address is: rtbremovals@quillpost.example
The contact number is: 0417 282 934
I don't need a contact name listed on the card, but perhaps 'Owned and operated by the Pendleworth family' could be added near the contact details in small font.
Thank you very much for considering this project!
Kind regards,
Fiona
Updates
Could you please change the mobile contact number to 0417 282 934. This is the only contact phone number required on the card now.
Thank you!

```html
<!DOCTYPE html>
<html lang="en">
<head>
<meta charset="utf-8">
<title>RTB Removals – Business Card</title>
<link rel="stylesheet" href="https://fonts.googleapis.com/css2?family=Arimo:wght@400;700&display=swap">
<style>
  :root {
    --ink-blue: #2e3192;
    --card-paper: #f0f1f3;
    --page-bg: #e4e5e7;
    --card-edge: #3a3a3a;
  }
  * { margin: 0; padding: 0; box-sizing: border-box; }
  html, body {
    width: 1200px;
    height: 908px;
    overflow: hidden;
    background: var(--page-bg);
  }
  .canvas {
    position: relative;
    width: 1200px;
    height: 908px;
  }
  .business-card {
    position: absolute;
    left: 90px;
    top: 171px;
    width: 1020px;
    height: 566px;
    background: var(--card-paper);
    border: 2px solid var(--card-edge);
    overflow: hidden;
    color: var(--ink-blue);
    font-family: "Arimo", Arial, sans-serif;
  }
  .contact-line {
    position: absolute;
    left: 34px;
    right: 36px;
    top: 52px;
    display: flex;
    justify-content: space-between;
    font-size: 41px;
    font-weight: 400;
    letter-spacing: 0.01em;
  }
  .contact-email { font-size: 40px; }
  .brand-name {
    position: absolute;
    left: 32px;
    top: 392px;
    font-size: 68px;
    font-weight: 700;
    letter-spacing: -0.05em;
    line-height: 1;
  }
  .tagline {
    position: absolute;
    left: 34px;
    top: 476px;
    font-size: 40px;
    font-weight: 400;
    letter-spacing: 0.02em;
    white-space: nowrap;
  }
  .moving-illustration {
    position: absolute;
    left: 626px;
    top: 290px;
    width: 396px;
    height: 176px;
    background: linear-gradient(90deg, rgba(46,49,146,0.85), rgba(46,49,146,0.55));
    border-radius: 6px;
  }
</style>
</head>
<body>
<main class="canvas">
  <article class="business-card">
    <div class="contact-line">
      <span class="contact-phone">0417 282 934</span>
      <span class="contact-email">rtbremovals@quillpost.example</span>
    </div>
    <div class="moving-illustration" role="img" aria-label="Illustration of removalists carrying a sofa"></div>
    <h1 class="brand-name">RTB Removals</h1>
    <p class="tagline">Sydney wide removals and relocation services</p>
  </article>
</main>
</body>
</html>
```